Brochure Design Project

We require a brochure design for ongoing marketing of our business / services.

Purpose - As a handout to support / summarise discussions when dealing with prospective clients face to face.

Aim - Should "sell" our business , summarise our capabilities & business focus. Assist in convincing clients that we are the best solution to their logistic needs.

Brochure size - A4 (ie printed on A3 double sided & folded)
Brochure finish - Glossy, colour , medium weight ( approx 140 gsm)

Suggested Content -
Front page - Profile / Intro to company
Centre pages - Capabilities / selling points
Rear page - Depot location map, contact details, reference to website

Should be brief on words, dot points ????
Insert some colour photos.

Reference Material -
Web site (www.ferncastlegroup.com.au)
Powerpoint presentation
business unit profiles ( Word Docs.)
Draft of brochure ( too many words , no photo's !!)

Industry/Entity Type

Marketing

```html
<!DOCTYPE html>
<html lang="en">
<head>
<meta charset="utf-8">
<title>Ferncastle Group – Capabilities Spread</title>
<link href="https://fonts.googleapis.com/css2?family=Questrial&family=Arimo:wght@400;700&display=swap" rel="stylesheet">
<style>
  :root{
    --stage:#e8e4de;
    --maroon:#5c0e12;
    --maroon-deep:#470a0d;
    --maroon-light:#6b1419;
    --gold:#f3d21c;
    --ink-light:#ffffff;
    --rule:#d9c9c9;
    --cream-top:#fbf6e6;
    --cream-bottom:#e9dfbf;
    --ink-dark:#2a1a14;
    --bullet:#b3181d;
  }
  *{box-sizing:border-box;margin:0;padding:0}
  html,body{width:1200px;height:900px;overflow:hidden;background:var(--stage)}
  body{font-family:"Arimo",Arial,sans-serif;color:var(--ink-light)}
  .spread{position:absolute;left:20px;top:40px;width:1160px;height:820px;display:flex;box-shadow:0 10px 30px rgba(0,0,0,.25)}
  .page{position:relative;width:580px;height:820px;overflow:hidden;background:linear-gradient(160deg,var(--maroon-light),var(--maroon) 45%,var(--maroon-deep))}
  .page--left{box-shadow:inset -18px 0 22px -14px rgba(0,0,0,.45)}
  .page--right{box-shadow:inset 18px 0 22px -14px rgba(0,0,0,.45)}
  .abs{position:absolute}
  .title{font-family:"Questrial","Century Gothic",sans-serif;color:var(--gold);font-weight:400;line-height:1.05}
  .title--xl{font-size:44px}
  .title--md{font-size:21px}
  .title--sm{font-size:17px}
  .body{font-size:10.5px;line-height:1.45}
  .body p{margin-bottom:8px}
  .body--small{font-size:8.6px;line-height:1.4}
  .body--small p{margin-bottom:6px}
  .photo{border:4px solid #fff;box-shadow:2px 3px 8px rgba(0,0,0,.5)}
  .rule{position:absolute;left:10px;right:10px;height:2px;background:var(--rule);opacity:.85}
  .photo--containers{background:linear-gradient(180deg,#a9bfd6 0%,#c8d3dc 40%,#8f8a80 60%,#5d5a55 100%)}
  .photo--sideloader{background:linear-gradient(180deg,#7fa6d2 0%,#b7cde4 45%,#9a9890 62%,#6b6862 100%)}
  .photo--truck{background:linear-gradient(180deg,#6f9fd6 0%,#aecbe8 48%,#c9c2ae 64%,#958c77 100%)}
  .photo--yard{background:linear-gradient(180deg,#4e6a3e 0%,#8a8f88 30%,#b9b6ae 60%,#e3e3de 100%)}
  .photo--forklift{background:linear-gradient(180deg,#8fb2d4 0%,#c7ccd0 40%,#7b7f77 70%,#3f6b4c 100%)}
  .photo--aerial{background:linear-gradient(170deg,#7f8a5a 0%,#8d7a52 35%,#6f7a48 60%,#9a8a62 80%,#5f7040 100%)}
  .services{position:absolute;left:300px;top:50px;width:235px;height:276px;border-radius:9px;
    background:linear-gradient(180deg,var(--cream-top),var(--cream-bottom));color:var(--ink-dark);
    padding:11px 14px;font-size:10px;line-height:1.38;box-shadow:2px 3px 8px rgba(0,0,0,.45)}
  .services ul{margin-top:7px;padding-left:26px}
  .services li{margin-bottom:2px}
  .services li::marker{color:var(--bullet)}
  strong{font-weight:700}
</style>
</head>
<body>
<div class="spread">
  <section class="page page--left">
    <h1 class="title title--xl abs" style="left:28px;top:34px">Overview</h1>
    <div class="body abs" style="left:28px;top:96px;width:285px">
      <p><strong>Ferncastle Group Pty Ltd.</strong> is a diverse, dynamic, and rapidly growing Transport &amp; Logistic company.</p>
      <p>Headquartered in Newcastle, and with a number of depots throughout New South Wales &amp; Queensland, Ferncastle Group is able to provide the complete logistic solution to customers throughout eastern Australia.</p>
      <p>Ferncastle Group today consists of a number of divisions including, <strong>Transport, Intermodal, Rural &amp; Industrial</strong> services.</p>
      <p>In all of these businesses Ferncastle Group is committed to the delivery of high quality service with a strong customer focus, underpinned by an overriding commitment to safety, the Chain of Responsibility legislation, and working with our customers to continually refine and improve service efficiencies.</p>
      <p>The Ferncastle Group team prides itself in working with clients to provide a transport partnership that delivers complete logistic solutions which encompass efficiency, value, compliance &amp; a customer focussed attitude.</p>
    </div>
    <div class="photo photo--containers abs" role="img" aria-label="Photo of a forklift moving a shipping container beside rail wagons" style="left:330px;top:36px;width:222px;height:200px"></div>
    <div class="photo photo--sideloader abs" role="img" aria-label="Photo of a side-loader truck lifting a container" style="left:330px;top:250px;width:222px;height:190px"></div>

    <div class="rule" style="top:456px"></div>

    <h2 class="title title--md abs" style="left:28px;top:470px">Transport</h2>
    <div class="body body--small abs" style="left:28px;top:498px;width:180px">
      <p>Our area of operation currently extends from South Australia to Far North Queensland, in support of commercial, industrial and rural based customers. The Ferncastle Group fleet includes a variety of standard bulk transport vehicles as well as general purpose, pressure and liquid tankers, container skels &amp; container tipping Skels</p>
      <p>This fleet is augmented by a large, long term sub-contractor fleet.</p>
      <p>The fleet is licensed under EPA requirements and a number of drivers hold dangerous goods licences and Maritime Services Identification Accreditation.</p>
      <p>Our company philosophy is to provide a timely well managed service compliant to all Legislative requirements. Through cooperative participation, we support our customers in the overall "chain of responsibility" process.</p>
    </div>
    <div class="photo photo--truck abs" role="img" aria-label="Photo of a semi-trailer truck loaded with steel on a flat road" style="left:220px;top:468px;width:334px;height:112px"></div>
    <div class="body body--small abs" style="left:220px;top:594px;width:162px">
      <p>Our industry accreditation through "Haulsafe" ensures that we maintain externally audited standards of Management, Maintenance, training and driver health.</p>
      <p>We are also accredited the National heavy Vehicle Accreditation Scheme for Mass, Maintenance &amp; Fatigue.</p>
      <h2 class="title title--sm" style="margin:6px 0 6px">Intermodal</h2>
      <p>Ferncastle Group operates rail sidings at Kooragang Island and Forbes. In both cases, these sidings are serviced by regular rail schedules</p>
    </div>
    <div class="body body--small abs" style="left:394px;top:594px;width:160px">
      <p>to and from Port Botany and cater primarily for the export of containerised freight. Services are not restricted to containerised freight and any type of freight can be moved in or out of any destination in Australia.</p>
      <p>All the required handling equipment is available as well as open and covered areas for packing and unpacking containers at our intermodal terminals. The Forbes depot is designed for the storage, value adding and containerisation of grain and rural produce for export.</p>
    </div>
  </section>

  <section class="page page--right">
    <h2 class="title title--sm abs" style="left:20px;top:36px;width:170px">Warehousing /<br>Distribution</h2>
    <div class="body body--small abs" style="left:20px;top:82px;width:170px">
      <p>Warehouse storage and management is available at Kooragang Island and Brisbane sites.</p>
      <p>Both sites cater for unpack, short &amp; long term undercover storage &amp; re delivery.</p>
      <p>This service can be integrated with our other services to provide a total logistics solution.</p>
    </div>
    <div class="photo photo--yard abs" role="img" aria-label="Photo of a container yard with warehouse sheds and a forklift" style="left:205px;top:28px;width:352px;height:182px"></div>

    <div class="rule" style="top:228px"></div>

    <div class="photo photo--forklift abs" role="img" aria-label="Photo of a forklift unloading a curtain-side truck" style="left:14px;top:248px;width:292px;height:182px"></div>
    <h2 class="title title--md abs" style="left:325px;top:266px">Industrial / Port<br>Related Activities</h2>
    <div class="body abs" style="left:325px;top:318px;width:235px;font-size:10.5px;line-height:1.6">
      <p>A wide range of industrial services is offered by Ferncastle Group that can be delivered individually or combined into a contract management package. Industrial services can be provided at one of our sites or your location.</p>
    </div>

    <div class="rule" style="top:448px"></div>

    <div class="photo photo--aerial abs" role="img" aria-label="Aerial photo of a rural depot with storage silos, sheds and a dam beside a highway" style="left:14px;top:462px;width:548px;height:346px">
      <div class="services">
        <p>Please contact us if you require a particular industrial service that is not on the following list of currently provided services.</p>
        <ul>
          <li>Bulk mineral storage, both covered and open air.</li>
          <li>Carbonaceous storage in lots up to 50,000 tonnes.</li>
          <li>Ship loading and discharge.</li>
          <li>Container packing and unpacking.</li>
          <li>Bulk material container loading facilities.</li>
          <li>Contract management, including storage and distribution.</li>
          <li>Just in time delivery of stored products to client users.</li>
          <li>Computerised stock management and control.</li>
          <li>Plant hire.</li>
        </ul>
      </div>
    </div>
  </section>
</div>
</body>
</html>
```